依頼概要
■ 依頼の目的/概要

ラーメンの通販サイトを運営しております。
どういった商品を扱っているかを説明したチラシの作成をお願い致します。
(テキストはこちらで用意してあります)

■ デザインへの要望

ラーメン画像を豊富に使用し、明るいイメージのものを希望しています。
(ラーメンチラシは黒や赤が多いのですが、そのイメージとは異なるもの)

テキスト・画像素材につきましては添付したファイルのものを使用ください。
画像素材が足りない場合は、その旨ご連絡下さい。
(テキストは必須ですが、画像の使用有無はお任せ致します。)

■サイズ

A4 両面 フルカラー

■ 納品ファイルの希望

Illustrator
※画像は埋め込んでください。
※選考後、アウトライン有無の両方を納品いただきたく存じます。

■ 利用用途

チラシのみ

■ 進め方

弊社の希望するイメージに近い提案を1つ(場合によって複数)選択させて頂きます。希望に近づけるために、修正要望を個別にさせて頂くこともあります。コンペ方式のため、修正後に当選されない場合も、どうかご了承ください。

■ その他/注意点

選択させて頂いたデザインの著作権(財産権)等の扱いはTovira利用規約に従い、弊社に譲渡をお願いします。フォントや画像素材などを利用する場合は上記利用用途に使用できることを確認し、第三者の知的財産権等に注意して下さい。

以後、別チラシ作成のお願いを直接させていただく事もございますため
継続してご相談させて頂く事が可能な方を希望致します。
■ 選んだ理由

弊社の想定していたイメージに一番近かったものを選択させて頂きました。

■ 提案者全員のお礼・コメント

この度はご提案いただき、誠にありがとうございました。
今後もこのような案件依頼をさせて頂く予定でございますので
その際にはまたご協力頂けましたら幸いです。

よろしくお願い致します。

```html
<!DOCTYPE html>
<html lang="ja">
<head>
<meta charset="utf-8">
<title>Shirutabi フライヤー</title>
<link rel="stylesheet" href="https://fonts.googleapis.com/css2?family=Noto+Sans+JP:wght@400;700;900&display=swap">
<style>
  :root{
    --red:#d8231f;
    --ink:#222222;
    --paper:#ffffff;
    --soup-a:#d9a25a;
    --soup-b:#8a4a22;
    --soup-c:#e8c98c;
    --bowl-bg:#3a2a20;
  }
  *{margin:0;padding:0;box-sizing:border-box;}
  html,body{width:846px;height:1200px;overflow:hidden;background:var(--paper);}
  body{font-family:"Noto Sans JP",sans-serif;color:var(--ink);position:relative;}

  .site-url{position:absolute;top:14px;right:40px;font-size:17px;letter-spacing:.5px;}
  .brand{position:absolute;top:40px;left:0;width:846px;text-align:center;}
  .brand-name{font-size:60px;font-weight:700;color:var(--ink);line-height:1;}

  .headline{position:absolute;top:132px;left:0;width:846px;text-align:center;font-size:29px;font-weight:700;letter-spacing:1px;}

  .photo-grid{position:absolute;left:28px;top:205px;width:410px;height:980px;
    display:grid;grid-template-columns:1fr 1fr;grid-template-rows:repeat(7,1fr);gap:6px;}
  .photo{border-radius:2px;}
  .photo.warm{background:radial-gradient(circle at 50% 50%,var(--soup-c) 0 38%,var(--soup-a) 55%,var(--bowl-bg) 85%);}
  .photo.deep{background:radial-gradient(circle at 50% 50%,var(--soup-a) 0 35%,var(--soup-b) 60%,var(--bowl-bg) 90%);}
  .photo.red{background:radial-gradient(circle at 50% 50%,#e07a3a 0 35%,#b23a1c 60%,var(--bowl-bg) 90%);}

  .points{position:absolute;left:452px;top:205px;width:370px;}
  .point{margin-bottom:28px;}
  .point-title{display:flex;gap:8px;color:var(--red);font-weight:700;font-size:19px;line-height:1.4;margin-bottom:8px;}
  .point-num{flex:none;width:24px;height:24px;margin-top:2px;border-radius:50%;background:var(--red);color:var(--paper);
    font-size:15px;display:flex;align-items:center;justify-content:center;}
  .point-body{font-size:15.5px;line-height:1.72;padding-left:2px;}
</style>
</head>
<body>
  <div class="site-url">http://www.shirutabi.example</div>
  <div class="brand"><span class="brand-name">Shirutabi</span></div>
  <h1 class="headline">店舗直送系ラーメン通販サイト「Shirutabi」って？</h1>

  <div class="photo-grid">
    <div class="photo warm" role="img" aria-label="醤油ラーメンの写真"></div>
    <div class="photo deep" role="img" aria-label="豚骨ラーメンの写真"></div>
    <div class="photo warm" role="img" aria-label="塩ラーメンの写真"></div>
    <div class="photo red" role="img" aria-label="辛味噌ラーメンの写真"></div>
    <div class="photo deep" role="img" aria-label="味噌ラーメンの写真"></div>
    <div class="photo warm" role="img" aria-label="中華そばの写真"></div>
    <div class="photo warm" role="img" aria-label="魚介ラーメンの写真"></div>
    <div class="photo deep" role="img" aria-label="家系ラーメンの写真"></div>
    <div class="photo red" role="img" aria-label="担々麺の写真"></div>
    <div class="photo warm" role="img" aria-label="鶏白湯ラーメンの写真"></div>
    <div class="photo deep" role="img" aria-label="つけ麺の写真"></div>
    <div class="photo warm" role="img" aria-label="煮干しラーメンの写真"></div>
    <div class="photo warm" role="img" aria-label="チャーシュー麺の写真"></div>
    <div class="photo deep" role="img" aria-label="濃厚豚骨魚介ラーメンの写真"></div>
  </div>

  <div class="points">
    <section class="point">
      <h2 class="point-title"><span class="point-num">1</span><span>行列のできる本物の味をご家庭で。</span></h2>
      <p class="point-body">シルタビでは日本中の行列のできる有名店の濃縮タイプのスープではなく、お店で出されるラーメンどんぶりの中のスープをそのまま冷凍してお届けしています。ご家庭で解凍するだけで、お店本来の美味しさを楽しめるスープです。</p>
    </section>
    <section class="point">
      <h2 class="point-title"><span class="point-num">2</span><span>なぜ粉末や濃縮タイプではなく、ストレートスープにこだわるのか。</span></h2>
      <p class="point-body">粉末タイプのスープは、粉をお湯に溶いてスープにするため、軽い味わいになりがちです。また、濃縮タイプはお店の味を薄めて再現するため、本来のコクや香りが損なわれてしまいます。ラーメン店で出されるスープは素材の旨みが詰まったデリケートなものです。少しでもお湯の量が違うだけで、味や風味が全く変わってしまいます。</p>
    </section>
    <section class="point">
      <h2 class="point-title"><span class="point-num">3</span><span>お店と同じこだわりの味を楽しむ事ができることが、ストレートスープの醍醐味。</span></h2>
      <p class="point-body">ストレートスープの場合、人気店で提供されるラーメン一杯のスープをそのまま急速冷凍しておりますので、お店の味そのままです。今までお店に並ばないと味わえなかった本物の味や風味がご家庭で楽しめます。自宅にいながらにして、お店と同じこだわりの味を楽しめることが、ストレートスープの醍醐味です。</p>
    </section>
    <section class="point">
      <h2 class="point-title"><span class="point-num">4</span><span>商品の到着までに若干、お時間をいただいております。</span></h2>
      <p class="point-body">ストレートスープは、お客様からご注文頂いた後に、一食分ずつ丁寧に手作りしてお届けしております。そのため、商品の到着までにお時間を頂いております。味が出来上がるまで待っていただく分、お店本来の味を楽しめるのが最大の特徴です！</p>
    </section>
  </div>
</body>
</html>
```